Business Card Design

New Homes
Renovations/Additions
Building Maintenance
Design
Council Approvals
Estimates
Project and Construction Management

The back of the card should only contain my logo which is attached and under the logo have written velta & velta constructions.

Industry/Entity Type

Business

Contact Information for Business Card

Company Name: Velta & Velta Constructions Pty Ltd
BLD 613072
ABN: 42 905 217 630
Position: Director
Name: Tarv Olukendri
Tel: m. 0418276034
f. (08)83126649
veltanvelta@mailpost.example

```html
<!DOCTYPE html>
<html lang="en">
<head>
<meta charset="UTF-8">
<title>Velta &amp; Velta Constructions — Business Card</title>
<link rel="stylesheet" href="https://fonts.googleapis.com/css2?family=Open+Sans:wght@300;400&family=PT+Serif&display=swap">
<style>
  :root {
    --page-bg: #e6e4e1;
    --card-white: #fbfbfb;
    --card-black: #0b0b0b;
    --ink: #161616;
    --ink-soft: #8a8a8a;
    --band-text: #d6d6d6;
    --shadow: rgba(0,0,0,0.22);
  }
  * { margin: 0; padding: 0; box-sizing: border-box; }
  html, body {
    width: 1200px; height: 677px; overflow: hidden;
    background: var(--page-bg);
    font-family: "Open Sans", Arial, sans-serif;
  }
  .canvas {
    position: relative; width: 1200px; height: 677px;
    display: flex; align-items: center; justify-content: center; gap: 60px;
  }
  .card {
    position: relative; width: 500px; height: 305px;
    background: var(--card-white);
    box-shadow: 0 10px 28px var(--shadow);
    overflow: hidden;
  }
  .card__band {
    position: absolute; left: 0; right: 0; bottom: 0; height: 78px;
    background: var(--card-black);
  }

  /* Front */
  .brand-mark {
    position: absolute; top: 22px; right: 26px;
    display: flex; align-items: center; gap: 8px;
    font-weight: 400; font-size: 13px; letter-spacing: 0.04em;
    color: var(--ink);
  }
  .brand-mark__circle {
    width: 22px; height: 22px; border: 2px solid var(--ink); border-radius: 50%;
  }
  .person {
    position: absolute; left: 34px; top: 118px;
  }
  .person__name {
    font-weight: 300; font-size: 27px; letter-spacing: 0.02em;
    color: var(--ink); line-height: 1.1;
  }
  .person__role {
    margin-top: 4px; margin-left: 150px;
    font-weight: 300; font-size: 12px; color: var(--ink-soft);
  }
  .contact {
    position: absolute; left: 34px; bottom: 11px;
    list-style: none;
    font-weight: 300; font-size: 13.5px; line-height: 19px;
    color: var(--band-text);
  }

  /* Back */
  .back-logo {
    position: absolute; left: 0; right: 0; top: 70px;
    display: flex; flex-direction: column; align-items: center; gap: 12px;
  }
  .back-logo__circle {
    width: 64px; height: 64px; border: 3px solid var(--ink); border-radius: 50%;
  }
  .back-logo__name {
    font-weight: 400; font-size: 16px; letter-spacing: 0.05em; color: var(--ink);
  }
  .back-title {
    position: absolute; left: 0; right: 0; bottom: 0; height: 78px;
    display: flex; align-items: center; justify-content: center;
    font-family: "PT Serif", Georgia, serif;
    font-size: 17px; letter-spacing: 0.03em; color: var(--band-text);
  }
</style>
</head>
<body>
<main class="canvas">

  <section class="card card--back" aria-label="Card back">
    <div class="back-logo">
      <span class="back-logo__circle"></span>
      <span class="back-logo__name">velta &amp; velta constructions</span>
    </div>
    <div class="card__band"></div>
    <p class="back-title">Velta &amp; Velta Constructions</p>
  </section>

  <section class="card card--front" aria-label="Card front">
    <div class="brand-mark">
      <span class="brand-mark__circle"></span>
      <span>velta &amp; velta</span>
    </div>
    <div class="person">
      <h1 class="person__name">TARV OLUKENDRI</h1>
      <p class="person__role">Director</p>
    </div>
    <div class="card__band"></div>
    <ul class="contact">
      <li>BLD 613072 ABN: 42 905 217 630</li>
      <li>Tel: m. 0418276034 f. (08)83126649</li>
      <li>veltanvelta@mailpost.example</li>
    </ul>
  </section>

</main>
</body>
</html>
```